Modern CNC Machining Facility in Need of Web Site Improvement

Brixton Fabrication and Tooling, LLC is in need of a web site update. We need to highlight both product sales and our manufacturing services offered. We have recently started offering online product sales and need a better ecommerce platform for our customers. We would like the design winner to be able to freelance the project to a fully functioning webpage.
www.brixtonfabrication.example
What we like about our current web site:
Black and red highlight colors
Gear and caliper logo
RNVR Veteran owned business
What we don't like about our current web site:
Unorganized
Doesn't stand out
Looks like it was made in 1995
Online Product sales are awkward

```html
<!DOCTYPE html>
<html lang="en">
<head>
<meta charset="utf-8">
<title>Brixton Fabrication and Tooling, LLC</title>
<link href="https://fonts.googleapis.com/css2?family=Roboto:wght@400;500;700&family=Roboto+Condensed:wght@500&display=swap" rel="stylesheet">
<style>
:root{
  --red:#a3181c;
  --red-dark:#8c1316;
  --ink:#222;
  --text:#555;
  --line:#d8d8d8;
  --navy:#182a3c;
  --white:#fff;
}
*{box-sizing:border-box;margin:0;padding:0}
html,body{width:973px;height:1200px;overflow:hidden;background:var(--white);font-family:"Roboto",Arial,sans-serif;color:var(--text)}
.page{position:relative;width:973px;height:1200px}
.abs{position:absolute}
.top-strip{left:0;top:0;width:973px;height:8px;background:var(--red)}
.brand{left:162px;top:17px;display:flex;align-items:center;gap:10px}
.brand-mark{width:70px;height:70px;border-radius:50%;background:var(--red)}
.brand-name{font-family:"Roboto Condensed",Arial,sans-serif;font-weight:500;font-size:18px;color:var(--red);text-transform:uppercase;letter-spacing:.2px}
.brand-tag{position:absolute;left:80px;top:45px;font-size:8.5px;color:#444;white-space:nowrap}
.call{left:674px;top:37px;display:flex;align-items:center}
.call-field{width:78px;height:17px;border:1px solid #ccc;font-size:7px;color:#222;padding:4px 12px}
.call-btn{width:58px;height:24px;background:var(--red);color:var(--white);font-size:8px;font-weight:700;display:flex;align-items:center;justify-content:center;gap:4px}
.nav{left:0;top:93px;width:973px;height:41px;background:var(--red);border-bottom:3px solid #6e1012}
.nav a{position:absolute;top:0;height:38px;line-height:38px;color:var(--white);font-size:8.5px;font-weight:500;text-decoration:none}
.nav .active{background:#2a2a2a;width:75px;text-align:center}
.hero{left:0;top:134px;width:973px;height:330px;background:radial-gradient(ellipse at 48% 50%,#d9d4cc 0,#a89e90 22%,#6e5844 45%,#3f2e24 80%)}
.hero-arrow{top:150px}
.hero-dots{left:464px;top:307px;display:flex;gap:3px}
.hero-dots i{width:9px;height:9px;border-radius:50%;background:var(--white);border:1px solid #555;display:block}
.hero-dots i.on{background:var(--red)}
.welcome{left:162px;top:476px;width:648px;text-align:center}
.welcome h1{font-size:15.5px;font-weight:400;color:var(--ink)}
.welcome h1 span{color:var(--red)}
.welcome p{margin-top:7px;font-size:7.6px;line-height:15.5px}
.section-title{font-size:15.5px;font-weight:400;color:var(--red)}
.products-head{left:161px;top:568px;width:649px;display:flex;align-items:center}
.products-head .rule{flex:1;height:1px;background:#bbb;margin:0 14px}
.card{top:605px;width:205px;height:238px;border:1px solid #ddd;border-top:3px solid #2a2a2a}
.card-img{height:115px;position:relative}
.price{position:absolute;right:0;bottom:0;background:#1e1e1e;color:var(--white);font-size:7.6px;padding:5px 10px}
.card h3{font-size:12px;font-weight:400;color:var(--ink);margin:9px 6px 0}
.card p{font-size:7.3px;line-height:15.5px;margin:6px 6px 0}
.card-btn{position:absolute;left:-1px;right:-1px;bottom:-1px;height:24px;background:var(--red);color:var(--white);font-size:9px;display:flex;align-items:center;justify-content:center}
.tile{top:917px;width:159px;height:110px;border:1px solid #ddd}
.tile-img{height:83px}
.tile span{display:block;text-align:center;font-size:7.6px;color:var(--ink);margin-top:10px}
.sale-dots{left:471px;top:1038px;display:flex;gap:8px}
.sale-dots i{width:7px;height:7px;border-radius:50%;background:#bbb;display:block}
.sale-dots i.on{background:var(--red)}
.features{left:161px;top:1061px;width:649px;height:49px;border:1px solid #ddd;background:linear-gradient(#fff 60%,#eee);display:flex}
.feature{flex:1;border-right:1px solid #ddd;display:flex;align-items:center;padding-left:8px;gap:10px}
.feature:last-child{border-right:0}
.feature b{display:block;font-size:9px;font-weight:500;color:#333}
.feature small{display:block;font-size:6.6px;color:#666;margin-top:3px}
.footer{left:0;top:1125px;width:973px;height:75px;background:var(--navy);color:var(--white)}
.footer-links{position:absolute;left:163px;top:16px;font-size:7.6px;font-weight:500}
.copyright{position:absolute;left:163px;top:39px;font-size:7.6px;font-weight:500}
.social{position:absolute;left:722px;top:20px;display:flex;gap:2px}
.social i{width:20px;height:20px;background:#3a5a7a;display:block}
</style>
</head>
<body>
<div class="page">
  <div class="abs top-strip"></div>

  <div class="abs brand">
    <div class="brand-mark"></div>
    <div class="brand-name">Brixton Fabrication and Tooling, LLC</div>
    <div class="brand-tag">CNC Milling &amp; Turning, Production Machining, Ice Fishing Spears</div>
  </div>

  <div class="abs call">
    <div class="call-field">555-555-555</div>
    <div class="call-btn">
      <svg width="14" height="14" viewBox="0 0 14 14"><circle cx="7" cy="7" r="6.2" fill="none" stroke="#fff" stroke-width="1.2"/><circle cx="7" cy="5.5" r="2.2" fill="#fff"/><path d="M3 11.5c1-2.3 7-2.3 8 0" fill="#fff"/></svg>
      Call Me
    </div>
  </div>

  <nav class="abs nav">
    <a class="active" style="left:162px">Home</a>
    <a style="left:243px">Online Products Sales</a>
    <a style="left:355px">Ice Fishing Spears</a>
    <a style="left:454px">About Us / Industries Served</a>
    <a style="left:588px">Equipment</a>
    <a style="left:661px">Contact us</a>
    <a style="left:733px">Blog</a>
  </nav>

  <div class="abs hero" role="img" aria-label="Close-up photograph of cut steel gears on an ornate bronze piece">
    <svg class="abs hero-arrow" style="left:62px" width="16" height="22" viewBox="0 0 16 22"><path d="M12 2 4 11l8 9" fill="none" stroke="#fff" stroke-width="3.5"/></svg>
    <svg class="abs hero-arrow" style="left:898px" width="16" height="22" viewBox="0 0 16 22"><path d="M4 2l8 9-8 9" fill="none" stroke="#fff" stroke-width="3.5"/></svg>
    <div class="abs hero-dots"><i class="on"></i><i></i><i></i><i></i></div>
  </div>

  <section class="abs welcome">
    <h1>Welcome To <span>Brixton Fabrication and Tooling, LLC</span></h1>
    <p>Lorem ipsum dolor sit amet, consectetur adipiscing elit. Nulla convallis egestas rhoncus. Donec facilisis fermentum sem, ac viverra ante luctus vel. Donec vel mauris quam. Lorem ipsum dolor sit amet, consectetur adipiscing elit. Nulla convallis egestas rhoncus. Donec facilisis fermentum sem, ac viverra ante luctus vel. Donec vel mauris quam. Lorem ipsum dolor sit amet, consectetur adipiscing elit. Nulla convallis egestas rhoncus. Donec facilisis fermentum sem, ac viverra ante luctus vel. Donec vel mauris quam.</p>
  </section>

  <div class="abs products-head">
    <h2 class="section-title">Products</h2>
    <div class="rule"></div>
    <svg width="18" height="12" viewBox="0 0 18 12"><path d="M7 1 2 6l5 5M11 1l5 5-5 5" fill="none" stroke="#222" stroke-width="2"/></svg>
  </div>

  <article class="abs card" style="left:162px">
    <div class="card-img" role="img" aria-label="Photograph of a rusted triple gear wall clock" style="background:linear-gradient(135deg,#d8d4cf,#7a4a30 45%,#a8a29a)"><span class="price">Price: $150.00</span></div>
    <h3>Triple Gear Clock</h3>
    <p>CNC Plasma cut gear clock with a rust patina. Clear coat finish. Material is 16ga steel. Approximate Dimensions are 21" x 13". Made in Michigan by Brixton Fabrication and Tooling, LLC</p>
    <div class="card-btn">Add to Cart</div>
  </article>
  <article class="abs card" style="left:384px">
    <div class="card-img" role="img" aria-label="Photograph of a steel clock with spread wings" style="background:linear-gradient(135deg,#e6e3df,#b8b2ac 50%,#dcd8d3)"><span class="price">Price: $150.00</span></div>
    <h3>Gear Clock with Wings</h3>
    <p>CNC Plasma cut gear clock with a rust patina. Clear coat finish. Material is 16ga steel. Approximate Dimensions are 21" x 13". Made in Michigan by Brixton Fabrication and Tooling, LLC</p>
    <div class="card-btn">Add to Cart</div>
  </article>
  <article class="abs card" style="left:605px">
    <div class="card-img" role="img" aria-label="Photograph of a polished steel sun clock" style="background:radial-gradient(circle at 50% 50%,#e8e8e8,#6a6a6a 45%,#2e2e2e)"><span class="price">Price: $150.00</span></div>
    <h3>Sun Clock</h3>
    <p>CNC Plasma cut gear clock with a rust patina. Clear coat finish. Material is 16ga steel. Approximate Dimensions are 21" x 13". Made in Michigan by Brixton Fabrication and Tooling, LLC</p>
    <div class="card-btn">Add to Cart</div>
  </article>

  <h2 class="abs section-title" style="left:161px;top:886px">Best Sale</h2>

  <div class="abs tile" style="left:162px"><div class="tile-img" role="img" aria-label="Photograph of a jewelled butterfly brooch" style="background:linear-gradient(135deg,#cfe0e6,#6d6a50 50%,#c9dbe2)"></div><span>Custom design section</span></div>
  <div class="abs tile" style="left:325px"><div class="tile-img" role="img" aria-label="Photograph of an antique clock face" style="background:linear-gradient(135deg,#8a8272,#d8d1c4 50%,#7a7064)"></div><span>Custom design section</span></div>
  <div class="abs tile" style="left:488px"><div class="tile-img" role="img" aria-label="Photograph of a clockwork assemblage" style="background:radial-gradient(circle,#9a8a70,#5a4530 55%,#e4e0da)"></div><span>Custom design section</span></div>
  <div class="abs tile" style="left:651px"><div class="tile-img" role="img" aria-label="Photograph of brass gears and charms" style="background:linear-gradient(135deg,#6a5038,#b08a4a 50%,#5c4330)"></div><span>Custom design section</span></div>

  <div class="abs sale-dots"><i class="on"></i><i></i><i></i></div>

  <div class="abs features">
    <div class="feature">
      <svg width="34" height="26" viewBox="0 0 34 26"><path d="M2 9h7M0 13h9M3 17h6" stroke="#c0181c" stroke-width="2"/><path d="M13 7l10-5 10 5v12l-10 5-10-5z" fill="none" stroke="#c0181c" stroke-width="2"/><path d="M13 7l10 5 10-5M23 12v12" fill="none" stroke="#c0181c" stroke-width="2"/></svg>
      <div><b>FREE SHIPPING</b><small>Sed ut perspiciatis unde omnis.</small></div>
    </div>
    <div class="feature">
      <svg width="34" height="26" viewBox="0 0 34 26"><rect x="6" y="3" width="22" height="22" fill="none" stroke="#c0181c" stroke-width="2"/><path d="M6 8h22M11 0v6M23 0v6" stroke="#c0181c" stroke-width="2"/><text x="17" y="21" text-anchor="middle" font-family="Roboto,sans-serif" font-size="10" font-weight="700" fill="#c0181c">20</text></svg>
      <div><b>DAILY PROMOTION</b><small>Sed ut perspiciatis unde omnis.</small></div>
    </div>
    <div class="feature">
      <svg width="34" height="26" viewBox="0 0 34 26"><circle cx="17" cy="13" r="11" fill="none" stroke="#c0181c" stroke-width="4"/><circle cx="17" cy="13" r="5" fill="none" stroke="#c0181c" stroke-width="2"/></svg>
      <div><b>24/7 CUSTOMER CARE</b><small>Sed ut perspiciatis unde omnis.</small></div>
    </div>
    <div class="feature">
      <svg width="34" height="26" viewBox="0 0 34 26"><path d="M17 1a12 11 0 1 1-6 20l-6 4 2-6A12 11 0 0 1 17 1z" fill="#c0181c"/><text x="17" y="17" text-anchor="middle" font-family="Roboto,sans-serif" font-size="13" font-weight="700" fill="#fff">?</text></svg>
      <div><b>LIVE CHAT WITH US</b><small>Sed ut perspiciatis unde omnis.</small></div>
    </div>
  </div>

  <footer class="abs footer">
    <div class="footer-links">Home | About | Practices | People | Events | Contact | Site Map | Privacy Policy</div>
    <div class="copyright">Copyright © 2014 Dr Hale Morrow. All Rights Reserved</div>
    <div class="social"><i></i><i></i><i></i><i></i></div>
  </footer>
</div>
</body>
</html>
```